Brightbuns Business Card Design

Our company is called Brightbuns. We manufacture confectionary snacks & frozen novelties. Our initial product portfolio includes frozen ice lollies/popsicles & stick ice cream bars.

We require a business card design.

Please use the attached Logo.

Please use an orange, brown, yellow colour code. You may choose any combination of the 3 or include all three. The logo however must remain orange.

Target Market(s)

Business card will be targeted at distributors of our products such as supermarket procurement managers, convenience store owners, wholesale distributors and merchandising agents.

Industry/Entity Type

Business

Requirements
Must have
• Kelvin Marsh_Director/ P.O.Box Westhollow 5172, Accra, Ghana / m: 00233(0)507318264/ e: kelvin.marsh@fernpost.co.uk

```html
<!DOCTYPE html>
<html lang="en">
<head>
<meta charset="utf-8">
<title>Brightbuns Business Card</title>
<link rel="stylesheet" href="https://fonts.googleapis.com/css2?family=PT+Sans+Narrow&display=swap">
<style>
  :root {
    --bg-light: #a48d70;
    --bg-mid: #8e7657;
    --bg-dark: #6f5940;
    --orange: #f47a35;
    --amber: #fbb03b;
    --yellow: #ffe600;
    --silver: #e8e2d8;
    --chocolate: #5a4128;
    --text-yellow: #fff200;
  }
  html, body {
    margin: 0;
    padding: 0;
    overflow: hidden;
    background: #ffffff;
  }
  .card {
    position: relative;
    width: 1200px;
    height: 705px;
    overflow: hidden;
    background: radial-gradient(ellipse 70% 75% at 45% 40%, var(--bg-light) 0%, var(--bg-mid) 55%, var(--bg-dark) 100%);
    font-family: "PT Sans Narrow", "Arial Narrow", sans-serif;
  }
  .swooshes {
    position: absolute;
    inset: 0;
    width: 1200px;
    height: 705px;
  }
  .brand-name {
    position: absolute;
    left: 70px;
    top: 240px;
    width: 720px;
    margin: 0;
    text-align: center;
    font-weight: 400;
    font-size: 170px;
    line-height: 1;
    color: var(--orange);
    letter-spacing: 1px;
  }
  .contact {
    position: absolute;
    right: 33px;
    top: 226px;
    text-align: right;
    color: var(--text-yellow);
  }
  .contact .name {
    margin: 0;
    font-size: 31px;
    line-height: 40px;
    font-weight: 400;
  }
  .contact .role {
    margin: 0 0 6px;
    font-size: 24px;
    line-height: 32px;
  }
  .contact .line {
    margin: 0;
    font-size: 28px;
    line-height: 43px;
    white-space: nowrap;
  }
  .contact .icon {
    display: inline-block;
    vertical-align: -3px;
    margin-right: 3px;
  }
</style>
</head>
<body>
<main class="card">
  <svg class="swooshes" viewBox="0 0 1200 705" aria-hidden="true">
    <g class="swoosh-top" fill="none" stroke-linecap="round">
      <path d="M-20 135 C 80 40, 200 18, 330 30 C 500 48, 600 110, 760 112 C 920 114, 1060 70, 1220 30" stroke="var(--orange)" stroke-width="8"/>
      <path d="M-20 142 C 80 48, 200 27, 330 39 C 500 57, 600 118, 760 120 C 920 122, 1060 78, 1220 38" stroke="var(--yellow)" stroke-width="7"/>
      <path d="M-20 149 C 80 56, 200 35, 330 47 C 500 64, 600 124, 760 126 C 920 128, 1060 85, 1220 45" stroke="var(--silver)" stroke-width="5"/>
      <path d="M-20 155 C 80 62, 200 42, 330 54 C 500 71, 600 130, 760 132 C 920 134, 1060 92, 1220 52" stroke="var(--chocolate)" stroke-width="5"/>
    </g>
    <g class="swoosh-bottom" fill="none" stroke-linecap="round">
      <path d="M-20 560 C 60 640, 180 690, 330 670 C 500 648, 600 585, 770 580 C 930 576, 1060 610, 1220 645" stroke="var(--chocolate)" stroke-width="5"/>
      <path d="M-20 566 C 60 646, 180 696, 330 676 C 500 654, 600 591, 770 586 C 930 582, 1060 616, 1220 651" stroke="var(--silver)" stroke-width="5"/>
      <path d="M-20 573 C 60 653, 180 703, 330 683 C 500 661, 600 598, 770 593 C 930 589, 1060 623, 1220 658" stroke="var(--orange)" stroke-width="7"/>
      <path d="M-20 581 C 60 661, 180 711, 330 691 C 500 669, 600 606, 770 601 C 930 597, 1060 631, 1220 666" stroke="var(--yellow)" stroke-width="8"/>
    </g>
  </svg>

  <h1 class="brand-name">Brightbuns</h1>

  <section class="contact">
    <p class="name">Kelvin Marsh</p>
    <p class="role">Director</p>
    <p class="line">
      <svg class="icon" width="20" height="26" viewBox="0 0 20 26" aria-hidden="true">
        <rect x="2" y="2" width="16" height="22" rx="2" fill="none" stroke="var(--text-yellow)" stroke-width="3"/>
        <rect x="8" y="19" width="4" height="2" fill="var(--text-yellow)"/>
      </svg> : 00233(0)507318264
    </p>
    <p class="line">
      <svg class="icon" width="18" height="26" viewBox="0 0 18 26" aria-hidden="true">
        <path d="M9 1 C 4 1, 1 5, 1 9 C 1 15, 9 25, 9 25 C 9 25, 17 15, 17 9 C 17 5, 14 1, 9 1 Z M9 6 A 3 3 0 1 1 9 12 A 3 3 0 1 1 9 6 Z" fill="var(--text-yellow)" fill-rule="evenodd"/>
      </svg> :P.O.Box Westhollow 5172,
    </p>
    <p class="line">Accra, Ghana</p>
    <p class="line">
      <svg class="icon" width="30" height="24" viewBox="0 0 30 24" aria-hidden="true">
        <path d="M2 10 L15 2 L28 10 L28 22 L2 22 Z M2 10 L15 17 L28 10 M2 22 L12 15 M28 22 L18 15" fill="none" stroke="var(--text-yellow)" stroke-width="2" stroke-linejoin="round"/>
      </svg>: kelvin.marsh@fernpost.co.uk
    </p>
  </section>
</main>
</body>
</html>
```